Lantern Above the Harbor ~ An Unbinding Passage for Versemakers

My book is called “Lantern Above the Harbor.” Its subtitle is “An Unbinding Passage for Versemakers.” It is a book about being a poet, writing poetry, and the ways in which poets are connected to both society and the central energy of the Universe. I want the cover design to be abstract and impressionistic. A suggestion of fireworks or a starburst would be a plus. To be consistent with the 3 other books I have published, I want the font for the title, as well as my name (Dorothea Halvik) to be Papyrus. The subtitle font can be something more plain and sans serif, like Arial or Franklin Gothic Book, probably in italics. As for color, I definitely want pale gold (angelic). Possible other complimentary colors could be either light or dark shades of gray, turquoise, rose, rust or red. I'm attaching the back cover text and also three pages from inside the book that have line drawings, to give an example of the interior artwork.
Updates

Forgot to mention: My book is a paperback. Its size will be 8.5" high and 5.5" wide. I'm self-publishing it, and it will be printed by Quillby Press in Nebraska, USA. It has 104 pages. I think you need the number of pages, in order to make the spine of the book the correct width.

Target Market(s)

My target market is people who write poetry or are interested in how poetry is written.

Industry/Entity Type

Poetry

Font styles to use
Sans Serif
Other font styles liked:
• Papyrus for the front cover. Arial or another sans serif font on the back cover.

Colors

Designer to choose colors to be used in the design.

Requirements
Must have
• My book cover needs to be inspiring and uplifting, as well as abstract and impressionistic, with kind of a "New Age" feel. I don't want anything that looks rigid and scholarly.
Nice to have
• The book talks about the connection poets have to the Universe and the Creative Energy at the center of everything. The cover should convey that Energy.
Should not have
• My cover should not be realistic, logical or straight-laced. I want something that feels free, imaginative and unfettered.

```html
<!DOCTYPE html>
<html lang="en">
<head>
<meta charset="utf-8">
<title>Lantern Above the Harbor – Cover Wrap</title>
<link href="https://fonts.googleapis.com/css2?family=Macondo&family=Noto+Sans:ital,wght@0,400;0,500;1,700&family=Roboto:wght@400&display=swap" rel="stylesheet">
<style>
  :root {
    --page-bg: #f4f4f4;
    --gold: #f5e8a8;
    --ink-light: #f6f2ea;
    --ink-dark: #1d1c1c;
    --sky-deep: #1f2f45;
    --teal: #3d8c95;
    --rose: #b86a6c;
    --rust: #e0703a;
    --glow: #fff6d8;
    --photo-tone: #b79a86;
  }
  * { box-sizing: border-box; margin: 0; padding: 0; }
  html, body { width: 1200px; height: 813px; overflow: hidden; background: var(--page-bg); }
  .wrap {
    position: absolute; left: 52px; top: 52px; width: 1096px; height: 709px; overflow: hidden;
  }
  .artwork {
    position: absolute; inset: 0;
    background:
      radial-gradient(ellipse 260px 230px at 826px 371px, var(--glow) 0%, #ffd27a 18%, rgba(232,122,60,0.85) 42%, rgba(184,106,108,0.4) 70%, rgba(184,106,108,0) 100%),
      radial-gradient(ellipse 620px 520px at 826px 371px, rgba(61,140,149,0.9) 0%, rgba(61,140,149,0.6) 50%, rgba(31,47,69,0) 100%),
      linear-gradient(160deg, #a4676c 0%, #3f7f8c 30%, #7a5b70 55%, #2b3e55 80%, var(--sky-deep) 100%);
  }
  .back-cover {
    position: absolute; left: 46px; top: 69px; width: 444px;
    font-family: "Noto Sans", sans-serif; color: var(--ink-light);
    font-size: 14.5px; line-height: 18px; text-align: center; letter-spacing: 0.4px;
  }
  .back-cover p { margin-bottom: 13px; }
  .back-cover .lede { padding: 0 40px; }
  .back-cover .book-title { font-weight: 700; font-style: italic; font-size: 17px; letter-spacing: 0; }
  .back-cover .summary { font-weight: 500; }
  .back-cover .chapters { margin-bottom: 17px; }
  .author-note { position: absolute; left: 39px; top: 517px; width: 460px; }
  .author-photo {
    position: absolute; left: 0; top: 0; width: 60px; height: 88px;
    background: linear-gradient(180deg, #cbb7a6, var(--photo-tone) 60%, #5f9a86);
  }
  .author-quote {
    position: absolute; left: 69px; top: 0; width: 395px;
    font-family: "Roboto", sans-serif; font-size: 14.4px; line-height: 18px; color: var(--ink-light);
  }
  .spine {
    position: absolute; left: 588px; top: 0; width: 30px; height: 709px;
  }
  .spine-line {
    position: absolute; left: 30px; transform-origin: 0 0; transform: rotate(90deg);
    white-space: nowrap; font-family: "Macondo", cursive; color: var(--gold); font-size: 27px; line-height: 30px;
  }
  .spine-line.title { top: 90px; }
  .spine-line.title small { font-size: 15px; }
  .spine-line.author { top: 446px; }
  .front-cover {
    position: absolute; left: 652px; top: 0; width: 444px; height: 709px; text-align: center;
  }
  .front-title { font-family: "Macondo", cursive; color: var(--gold); font-weight: 400; }
  .front-title .big { display: block; font-size: 84px; line-height: 84px; }
  .front-title .small { display: block; font-size: 36px; line-height: 36px; }
  .front-title .line1 { margin-top: 52px; }
  .front-subtitle {
    margin-top: 20px; font-family: "Noto Sans", sans-serif; font-size: 26px; line-height: 36px;
    letter-spacing: 1.5px; color: var(--ink-dark);
  }
  .front-author {
    position: absolute; left: 0; right: 0; top: 604px;
    font-family: "Macondo", cursive; color: var(--gold); font-size: 52px; line-height: 60px;
  }
</style>
</head>
<body>
<div class="wrap">
  <div class="artwork" role="img" aria-label="Abstract impressionistic painting: a golden starburst of energy radiating rays of rust, rose and turquoise across a deep blue sky"></div>

  <section class="back-cover">
    <p class="lede"><span class="book-title">Lantern Above the Harbor</span> is indeed “An Unbinding Passage for Versemakers.” It is written by Dorothea Halvik, an exciting, imaginative voice in American poetry.</p>
    <p class="summary">In <span class="book-title">Lantern Above the Harbor,</span> Dorothea discusses the essential elements of poetry and the process of writing it. She offers an inspiring view of the mission of poets and their connection to both society and the larger forces in the Universe. Her book is motivational, refreshing and irrepressibly optimistic</p>
    <p class="chapters">The seven intriguing chapters in Lantern Above the Harbor are LIBERATION ~ EXPERIENCE ~ WORDS ~ POETRY ~ INTEGRITY ~ BEAUTY ~ CREATION</p>
    <p class="bio">For over 50 years, Dorothea has been a teacher of writing and poetry. Since 2007, she has published three books of her poems: Mind the Rain Barrel, The Pale Hem of Forever and The Wide Velvet Hush. Her work overflows with her characteristically rich images and quirky metaphors. It runs the gamut from subtle eroticism to abject grief, from defiant rage to philosophical meditation, and from borderline blasphemy to lyrical fantasy.</p>
  </section>

  <div class="author-note">
    <div class="author-photo" role="img" aria-label="Portrait photograph of the author"></div>
    <p class="author-quote">Dorothea has been called by critic Russell Danforth “a poet to be reckoned with; bright, feisty, compassionate.” (The Valley Courier, Milbrook, OH). Author Lenora Quaile (“Ashgrove,” 2011) says Dorothea’s poetry is like “a perpetual Surprise Party ~ memorable, insightful and thematically fascinating.”</p>
  </div>

  <div class="spine">
    <div class="spine-line title">Lantern <small>above the</small> Harbor</div>
    <div class="spine-line author">Dorothea Halvik</div>
  </div>

  <section class="front-cover">
    <h1 class="front-title">
      <span class="big line1">Lantern</span>
      <span class="small">above the</span>
      <span class="big">Harbor</span>
    </h1>
    <p class="front-subtitle">An Unbinding Passage<br>for Versemakers</p>
    <p class="front-author">Dorothea Halvik</p>
  </section>
</div>
</body>
</html>
```